Brellow Business Card Re-design

Our current cards are outdated. This is our website www.brellowinsight.com. We would like something that is "on-brand" and consistent with our social media sites. We are strategic consultants with a core competency in Marketing Research. Although, please know we are considering a brand logo redesign and potentially a new look. If we like your work here we will invite you to participate when we get to that project. Thank you very much. Corabel
Here are our social sites: https://chirvalo.com/Brellow?lang=en
https://plus.quarnix.com/+Brellowinsight
https://www.workvelt.com/company/4958207/
https://www.friendlumo.com/BrellowInc/
Project Deadline Extended Reason: We appreciate the designs that have been submitted. We are extending the deadline because not everyone in our office has been available until now to view the designs. Thank you. Added Monday, September 25, 2017
Industry/Entity Type
Business
Look and feel

```html
<!DOCTYPE html>
<html lang="en">
<head>
<meta charset="utf-8">
<title>Brellow Business Card</title>
<link rel="stylesheet" href="https://fonts.googleapis.com/css2?family=Arvo:wght@400;700&display=swap">
<style>
  :root {
    --lime: #c5d82e;
    --charcoal: #3e3e40;
    --paper: #ffffff;
    --service-grey: #cfcfcf;
    --icon-grey: #8a8a8c;
    --backdrop: #3a3a3b;
    --ink: #3e3e40;
  }
  * { margin: 0; padding: 0; box-sizing: border-box; }
  html, body { width: 1200px; height: 1200px; overflow: hidden; }
  body {
    background: var(--backdrop);
    font-family: "Arvo", Georgia, serif;
    position: relative;
  }
  .card {
    position: absolute;
    left: 150px;
    width: 900px;
    height: 490px;
    border-radius: 40px;
    overflow: hidden;
  }
  .card-front { top: 70px; background: var(--paper); }
  .card-back { top: 640px; background: var(--charcoal); }

  .front-panel { position: absolute; inset: 0; }

  .brand-block {
    position: absolute;
    left: 0;
    top: 42px;
    width: 470px;
    text-align: left;
    padding-left: 130px;
  }
  .brand-dot {
    width: 64px; height: 64px;
    border-radius: 50%;
    background: var(--charcoal);
    margin-left: 60px;
    margin-bottom: 18px;
  }
  .brand-name {
    font-weight: 700;
    font-size: 50px;
    line-height: 1;
    color: var(--charcoal);
  }

  .contact-list {
    position: absolute;
    left: 30px;
    top: 270px;
    list-style: none;
    color: var(--ink);
    font-size: 23px;
    line-height: 36px;
  }
  .contact-list li { display: flex; align-items: flex-start; }
  .contact-list svg { width: 24px; height: 24px; margin: 6px 12px 0 0; flex: none; }
  .contact-list .indent { padding-left: 36px; }

  .service-list {
    position: absolute;
    right: 28px;
    top: 44px;
    list-style: none;
    text-align: right;
    color: var(--service-grey);
    font-size: 23px;
    line-height: 45.6px;
  }
  .service-list li::after {
    content: "";
    display: inline-block;
    width: 0; height: 0;
    margin-left: 12px;
    border-top: 9px solid transparent;
    border-bottom: 9px solid transparent;
    border-right: 12px solid var(--lime);
    vertical-align: -2px;
  }

  .back-brand {
    position: absolute;
    left: 0; right: 0;
    top: 60px;
    text-align: center;
  }
  .back-dot {
    width: 120px; height: 120px;
    border-radius: 50%;
    background: var(--paper);
    margin: 0 auto 26px;
  }
  .back-name {
    font-weight: 700;
    font-size: 96px;
    line-height: 0.95;
    color: var(--lime);
  }
  .tagline {
    font-size: 17.5px;
    letter-spacing: 1.5px;
    color: var(--paper);
    margin-top: 6px;
    text-transform: uppercase;
  }
  .social-row {
    display: flex;
    justify-content: center;
    gap: 30px;
    margin-top: 30px;
    list-style: none;
  }
  .social-row li {
    width: 38px; height: 38px;
    border-radius: 50%;
    background: var(--icon-grey);
  }
</style>
</head>
<body>

<section class="card card-front">
  <svg class="front-panel" width="900" height="490" viewBox="0 0 900 490" aria-hidden="true">
    <path d="M 530 0 Q 400 250 545 490 L 900 490 L 900 0 Z" fill="var(--charcoal)"/>
  </svg>

  <div class="brand-block">
    <div class="brand-dot"></div>
    <div class="brand-name">brellow</div>
  </div>

  <ul class="contact-list">
    <li>
      <svg viewBox="0 0 24 24"><path d="M6.6 10.8a15 15 0 0 0 6.6 6.6l2.2-2.2a1 1 0 0 1 1-.25 11.4 11.4 0 0 0 3.6.6 1 1 0 0 1 1 1V20a1 1 0 0 1-1 1A17 17 0 0 1 3 4a1 1 0 0 1 1-1h3.5a1 1 0 0 1 1 1c0 1.25.2 2.45.6 3.6a1 1 0 0 1-.25 1z" fill="var(--lime)"/></svg>
      +1 555-210-4187
    </li>
    <li>
      <svg viewBox="0 0 24 24"><rect x="2" y="5" width="20" height="14" fill="var(--lime)"/><path d="M2 5 L12 13 L22 5" fill="none" stroke="#fff" stroke-width="1.6"/></svg>
      info@brellowinsight.com
    </li>
    <li>
      <svg viewBox="0 0 24 24"><path d="M12 2a7 7 0 0 0-7 7c0 5.2 7 13 7 13s7-7.8 7-13a7 7 0 0 0-7-7z" fill="var(--lime)"/><circle cx="12" cy="9" r="2.6" fill="#fff"/></svg>
      4820 Harbor Crest Blvd, Ste 210A
    </li>
    <li class="indent">Lakeview, Florida</li>
    <li>
      <svg viewBox="0 0 24 24"><circle cx="12" cy="12" r="10" fill="var(--lime)"/><path d="M2 12h20M12 2c3 3 3 17 0 20M12 2c-3 3-3 17 0 20" fill="none" stroke="#fff" stroke-width="1.3"/></svg>
      BrellowInsight.com
    </li>
  </ul>

  <ul class="service-list">
    <li>Strategic Visioning</li>
    <li>Customer Experience</li>
    <li>Operational Excellence</li>
    <li>C-Level &amp; Executive Serv.</li>
    <li>Marketing Research</li>
    <li>Behavioral Analysis</li>
    <li>Creative Branding</li>
    <li>Statistical Analysis</li>
    <li>Kid Research</li>
  </ul>
</section>

<section class="card card-back">
  <div class="back-brand">
    <div class="back-dot"></div>
    <div class="back-name">brellow</div>
    <div class="tagline">Strategic Marketing &amp; Market Research</div>
    <ul class="social-row" aria-label="Social profiles">
      <li></li><li></li><li></li><li></li><li></li>
    </ul>
  </div>
</section>

</body>
</html>
```